Hargrove Orthopedics and Sports Medicine
Arthroscopy of the Knee and Shoulder
Hargrove Orthopedics and Sports Medicine -
Creative Brief
Cutting-Edge
Daniel K. Hargrove Jr., M.D.
418 North Pelham Street Brayfield, AR 72819
quillmoth@mailvane.com
hargrovemd.com
under web address please add linkvane.net/hargrovemd Do not put email on the card
use large pic of logo or use another idea if you like

```html
<!DOCTYPE html>
<html lang="en">
<head>
<meta charset="utf-8">
<title>Hargrove Orthopedics and Sports Medicine – Business Card</title>
<link rel="stylesheet" href="https://fonts.googleapis.com/css2?family=Source+Sans+3:ital,wght@0,400;0,600;0,700;1,400&display=swap">
<style>
  :root {
    --page-bg: #e6e6e9;
    --card-white: #ffffff;
    --brand-navy: #1d3f8f;
    --brand-blue: #2f56a8;
    --band-deep: #173479;
    --band-light: #4a6fc0;
    --rule-grey: #c4c7cf;
    --muted-blue: #5a6a8c;
    --on-band: #ffffff;
  }
  * { box-sizing: border-box; margin: 0; padding: 0; }
  html, body {
    width: 1200px;
    height: 780px;
    overflow: hidden;
    background: var(--page-bg);
    font-family: "Source Sans 3", "Helvetica Neue", Arial, sans-serif;
  }
  .business-card {
    position: absolute;
    left: 75px;
    top: 90px;
    width: 1050px;
    height: 600px;
    border-radius: 30px;
    background: var(--card-white);
    overflow: hidden;
    box-shadow: 0 10px 30px rgba(20, 30, 60, 0.18);
  }
  .card-swoosh {
    position: absolute;
    inset: 0;
    width: 100%;
    height: 100%;
  }
  .doctor-block {
    position: absolute;
    top: 36px;
    right: 44px;
    text-align: right;
  }
  .doctor-name {
    font-size: 35px;
    font-weight: 700;
    color: var(--brand-navy);
    line-height: 1.1;
  }
  .doctor-specialty {
    font-size: 23px;
    font-weight: 400;
    color: var(--muted-blue);
    margin-top: 4px;
  }
  .practice-mark {
    position: absolute;
    left: 70px;
    top: 200px;
    display: flex;
    align-items: center;
    gap: 22px;
  }
  .practice-dot {
    width: 64px;
    height: 64px;
    border-radius: 50%;
    background: var(--brand-blue);
    flex: none;
  }
  .practice-name {
    color: var(--brand-navy);
    font-weight: 700;
    line-height: 1;
  }
  .practice-name .practice-main {
    display: block;
    font-size: 84px;
    letter-spacing: -1px;
  }
  .practice-name .practice-sub {
    display: block;
    font-size: 21px;
    letter-spacing: 1.2px;
    text-transform: uppercase;
    margin-top: 6px;
  }
  .contact-block {
    position: absolute;
    right: 44px;
    top: 345px;
    text-align: right;
    color: var(--on-band);
  }
  .postal-address {
    font-style: normal;
    font-size: 25px;
    line-height: 1.3;
  }
  .contact-row {
    display: flex;
    justify-content: flex-end;
    align-items: center;
    gap: 34px;
    font-size: 25px;
  }
  .contact-row.phones { margin-top: 40px; }
  .contact-row.web { margin-top: 26px; }
  .contact-item {
    display: flex;
    align-items: center;
    gap: 10px;
    white-space: nowrap;
  }
  .contact-icon {
    width: 26px;
    height: 26px;
    flex: none;
  }
</style>
</head>
<body>
  <main class="business-card">
    <svg class="card-swoosh" viewBox="0 0 1050 600" preserveAspectRatio="none" aria-hidden="true">
      <defs>
        <linearGradient id="bandGradient" x1="0" y1="1" x2="1" y2="0">
          <stop offset="0" stop-color="var(--band-deep)"/>
          <stop offset="0.6" stop-color="var(--brand-blue)"/>
          <stop offset="1" stop-color="var(--band-light)"/>
        </linearGradient>
      </defs>
      <path d="M0,545 C400,525 700,345 1050,118" fill="none" stroke="var(--rule-grey)" stroke-width="10"/>
      <path d="M0,600 L0,562 C400,542 700,362 1050,140 L1050,600 Z" fill="url(#bandGradient)"/>
    </svg>

    <header class="doctor-block">
      <h1 class="doctor-name">Daniel K. Hargrove Jr., M.D.</h1>
      <p class="doctor-specialty">Arthroscopy of the Knee and Shoulder</p>
    </header>

    <div class="practice-mark">
      <span class="practice-dot"></span>
      <p class="practice-name">
        <span class="practice-main">Hargrove</span>
        <span class="practice-sub">Orthopedics and Sports Medicine</span>
      </p>
    </div>

    <section class="contact-block">
      <address class="postal-address">
        418 North Pelham Street<br>
        Brayfield, AR 72819
      </address>

      <div class="contact-row phones">
        <span class="contact-item">
          <svg class="contact-icon" viewBox="0 0 24 24" aria-label="Phone">
            <path fill="#fff" d="M6.6 10.8a15.1 15.1 0 0 0 6.6 6.6l2.2-2.2a1 1 0 0 1 1-.25 11.4 11.4 0 0 0 3.6.57 1 1 0 0 1 1 1V20a1 1 0 0 1-1 1A17 17 0 0 1 3 4a1 1 0 0 1 1-1h3.5a1 1 0 0 1 1 1 11.4 11.4 0 0 0 .57 3.6 1 1 0 0 1-.25 1z"/>
          </svg>
          555 210 0142
        </span>
        <span class="contact-item">
          <svg class="contact-icon" viewBox="0 0 24 24" aria-label="Fax">
            <rect x="6" y="2" width="12" height="6" fill="#fff"/>
            <rect x="2" y="9" width="20" height="9" rx="2" fill="#fff"/>
            <rect x="6" y="14" width="12" height="8" fill="#fff" stroke="var(--brand-blue)" stroke-width="1.5"/>
          </svg>
          555 210 0143
        </span>
      </div>

      <div class="contact-row web">
        <span class="contact-item">
          <svg class="contact-icon" viewBox="0 0 24 24" aria-label="Website">
            <circle cx="12" cy="12" r="10" fill="none" stroke="#fff" stroke-width="2"/>
            <ellipse cx="12" cy="12" rx="4.5" ry="10" fill="none" stroke="#fff" stroke-width="1.6"/>
            <line x1="2" y1="12" x2="22" y2="12" stroke="#fff" stroke-width="1.6"/>
          </svg>
          hargrovemd.com
        </span>
        <span class="contact-item">
          <svg class="contact-icon" viewBox="0 0 24 24" aria-label="Social page">
            <circle cx="12" cy="12" r="10" fill="none" stroke="#fff" stroke-width="2"/>
            <ellipse cx="12" cy="12" rx="4.5" ry="10" fill="none" stroke="#fff" stroke-width="1.6"/>
            <line x1="2" y1="12" x2="22" y2="12" stroke="#fff" stroke-width="1.6"/>
          </svg>
          linkvane.net/hargrovemd
        </span>
      </div>
    </section>
  </main>
</body>
</html>
```